"Sun On Water" Gospel Presentation Booklet

I need a design for a 12 page (including front/back cover) square booklet, with religious images and aesthetically pleasing fonts/designs. I want it to be very simple, and very straightforward. The main focus of the project is it's content. So the design should be very nice, but also should point to the content, not take away from it, or create distraction. People should be more focused on the words than the imagery.

I enjoy modern designs, I need a sharp aesthetic that is clean and neat. Nothing over the top.
I have attached a word document with the content I would like on the pages.

Colors
0592cd
0255a3
33a6d7
85cae6
85acd3
3276b5
9bcb3b
f04a50
f68d4c

Requirements
Should not have
• Super feminine colors/aesthetics

```html
<!DOCTYPE html>
<html lang="en">
<head>
<meta charset="utf-8">
<title>Sun On Water – Gospel Booklet Spreads</title>
<link rel="stylesheet" href="https://fonts.googleapis.com/css2?family=Abel&family=Big+Shoulders+Display:wght@800&family=Fjalla+One&display=swap">
<style>
  :root {
    --ink: #0255a3;
    --ink-mid: #3276b5;
    --sky-deep: #7fc3e8;
    --sky-light: #cfe9f7;
    --cloud: #ffffff;
    --stage: #2b2b2b;
    --box-bg: #ffffff;
  }
  * { box-sizing: border-box; margin: 0; padding: 0; }
  html, body { width: 1200px; height: 923px; overflow: hidden; background: var(--stage); }
  .sheet { position: relative; width: 1200px; height: 923px; }

  .spread { position: absolute; width: 532px; height: 265px; overflow: hidden; }
  .col-left { left: 62px; }
  .col-right { left: 607px; }
  .row-1 { top: 44px; }
  .row-2 { top: 329px; }
  .row-3 { top: 613px; }

  .sky {
    position: absolute; inset: 0;
    background:
      radial-gradient(ellipse 180px 150px at 100px 40px, rgba(255,255,255,.85), rgba(255,255,255,0) 70%),
      linear-gradient(180deg, var(--sky-deep) 0%, var(--sky-light) 55%, var(--cloud) 100%);
  }
  .sky--cover {
    background:
      radial-gradient(ellipse 150px 200px at 420px 30px, rgba(255,255,255,.95), rgba(255,255,255,0) 70%),
      linear-gradient(180deg, #a9cfe6 0%, #dcebf5 50%, #eef5fa 100%);
  }

  .headword {
    position: absolute; left: 0; top: 0; width: 268px; height: 100%;
    display: flex; align-items: center; justify-content: center;
    font-family: "Big Shoulders Display", "Oswald", sans-serif; font-weight: 800;
    color: var(--ink); line-height: 1; text-transform: uppercase;
  }
  .headword--god { font-size: 128px; }
  .headword--man { font-size: 124px; }
  .headword--problem { font-size: 74px; }
  .headword--savior { font-size: 84px; }
  .headword--response { font-size: 70px; }

  .text-box {
    position: absolute; left: 295px; top: 30px; width: 206px; height: 206px;
    background: var(--box-bg);
    border: 1px solid var(--ink);
    outline: 1px solid var(--ink); outline-offset: -5px;
    display: flex; flex-direction: column; align-items: center; justify-content: center;
    padding: 14px 24px; text-align: center;
    font-family: "Abel", sans-serif; color: var(--ink);
  }
  .text-box--dense { padding: 12px 20px; }
  .icon {
    width: 30px; height: 30px; border-radius: 50%;
    background: var(--ink-mid); margin-bottom: 10px; flex: none;
  }
  .copy--lg { font-size: 17px; line-height: 1.38; }
  .copy--md { font-size: 11.5px; line-height: 1.4; }
  .copy--sm { font-size: 10.5px; line-height: 1.4; }
  .copy--md p + p { margin-top: 12px; }
  .steps { list-style: none; font-size: 8.6px; line-height: 1.35; }
  .steps li { margin-top: 5px; }
  .steps .lead { margin: 0 0 3px; }
  .divider { width: 110px; border-top: 1px dotted var(--ink); margin: 8px 0; }
  .call { font-family: "Fjalla One", sans-serif; font-size: 10.5px; line-height: 1.6; }

  .cover-box {
    position: absolute; left: 295px; top: 30px; width: 206px; height: 206px;
    background: rgba(255,255,255,.25);
    border: 1px solid var(--ink);
    outline: 1px solid var(--ink); outline-offset: -5px;
    display: flex; flex-direction: column; align-items: center; justify-content: center;
    font-family: "Big Shoulders Display", sans-serif; font-weight: 800; color: var(--ink);
    line-height: .92; text-align: center;
  }
  .cover-mark {
    position: absolute; left: 392px; top: 22px; width: 12px; height: 24px;
    background: var(--ink-mid); border-radius: 2px;
  }
  .cover-title__top { font-size: 62px; }
  .cover-title__main { font-size: 74px; text-transform: uppercase; }
</style>
</head>
<body>
<main class="sheet">

  <section class="spread col-left row-1" aria-label="Cover">
    <div class="sky sky--cover" role="img" aria-label="Bright sky above the clouds with light rays"></div>
    <div class="cover-box">
      <h1><span class="cover-title__top">Sun On</span><br><span class="cover-title__main">Water</span></h1>
    </div>
    <div class="cover-mark" role="img" aria-label="Small cross emblem"></div>
  </section>

  <section class="spread col-right row-1" aria-label="God">
    <div class="sky" role="img" aria-label="Soft blue sky with clouds and light glow"></div>
    <h2 class="headword headword--god">God</h2>
    <div class="text-box">
      <div class="icon" role="img" aria-label="Dove icon"></div>
      <p class="copy--lg">God is holy, that means He's perfect. In fact, He is so perfect, corruption cannot live with Him.</p>
    </div>
  </section>

  <section class="spread col-left row-2" aria-label="Man">
    <div class="sky" role="img" aria-label="Soft blue sky with clouds and light glow"></div>
    <h2 class="headword headword--man">Man</h2>
    <div class="text-box">
      <div class="icon" role="img" aria-label="Praying hands icon"></div>
      <p class="copy--lg">On the other hand, mankind is corrupt. For example, we are selfish, we are prideful, and we lie.</p>
    </div>
  </section>

  <section class="spread col-right row-2" aria-label="Problem">
    <div class="sky" role="img" aria-label="Soft blue sky with clouds and light glow"></div>
    <h2 class="headword headword--problem">Problem</h2>
    <div class="text-box text-box--dense">
      <div class="icon" role="img" aria-label="Flame icon"></div>
      <p class="copy--sm">And there is our big problem: if God is perfect and corruption cannot live with him… and we are corrupt… WE cannot live with God. Our corruption has cut us off from God… now… AND when we die which means we must spend eternity in a place called hell…</p>
    </div>
  </section>

  <section class="spread col-left row-3" aria-label="Savior">
    <div class="sky" role="img" aria-label="Soft blue sky with clouds and light glow"></div>
    <h2 class="headword headword--savior">Savior</h2>
    <div class="text-box text-box--dense">
      <div class="icon" role="img" aria-label="Small portrait illustration"></div>
      <div class="copy--md">
        <p>But that is not what God wants.</p>
        <p>God loves you so much he gave up his only Son to save you. The Redeemer died on the cross in our place to pay for our sin and rose again on the 3rd day.</p>
      </div>
    </div>
  </section>

  <section class="spread col-right row-3" aria-label="Response">
    <div class="sky" role="img" aria-label="Soft blue sky with clouds and light glow"></div>
    <h2 class="headword headword--response">Response</h2>
    <div class="text-box text-box--dense">
      <ol class="steps">
        <li class="lead">So now if anyone:</li>
        <li>1. Agrees with God they are corrupt.</li>
        <li>2. Believes the Redeemer will save them.</li>
        <li>3. And accepts Him as their personal Lord and Savior, the Redeemer will forgive their corruption, reconcile them to God, and come and live inside them.</li>
      </ol>
      <div class="divider"></div>
      <p class="call">You can pray to the Redeemer right now and ask him to save you using the above three steps as your prayer guide.</p>
    </div>
  </section>

</main>
</body>
</html>
```